International tradind company needs a professional Business Card

We are an international trading company and we need a business card for our CEO and employers so they can give it away in their meetings and while networking.
We want the card design quality to cause an immediate "wow" and we count on you to do that!

key-words and concepts to communicate: trustworthiness, ethics, sucess, modern, global business, networking

Our favorite colours are blue and grey but we are open to suggestions.

It would be recommended that our logo was part of the card. You can see it in www.kovendagroup.com . We also would like the following info on the card:
Name
position in the company
cell phone and personal email

```html
<!DOCTYPE html>
<html lang="en">
<head>
<meta charset="utf-8">
<title>Kovenda Group — Business Cards</title>
<link rel="stylesheet" href="https://fonts.googleapis.com/css2?family=Open+Sans:wght@400;600&display=swap">
<style>
  :root {
    --backdrop: #e6e7ea;
    --card-white: #f7f7f6;
    --brand-blue: #2f4f9a;
    --band-grey: #3a3b3e;
    --ink-navy: #1f2a5c;
    --accent-blue: #3f6fc0;
    --rule-grey: #555a66;
  }
  * { box-sizing: border-box; margin: 0; padding: 0; }
  html, body {
    width: 1200px; height: 873px; overflow: hidden;
    background: var(--backdrop);
    font-family: "Open Sans", Arial, sans-serif;
  }
  .canvas { position: relative; width: 1200px; height: 873px; }
  .card {
    position: absolute; top: 286px;
    width: 520px; height: 300px;
    background: var(--card-white);
    overflow: hidden;
    box-shadow: 0 6px 18px rgba(0,0,0,0.18);
  }
  .card--front { left: 60px; }
  .card--back { left: 620px; }
  .card__band { position: absolute; inset: 0; width: 520px; height: 300px; }
  .brand { position: absolute; display: flex; align-items: center; gap: 10px; }
  .brand__dot {
    width: 34px; height: 34px; border-radius: 50%;
    background: var(--brand-blue);
  }
  .brand__name {
    font-size: 30px; font-weight: 400; color: var(--ink-navy);
    letter-spacing: 0.2px; line-height: 1;
  }
  .tagline {
    position: absolute; font-size: 14px; color: var(--accent-blue);
  }
  .website {
    position: absolute; font-size: 12px; font-style: normal; color: var(--accent-blue);
  }
  .card--front .brand { left: 218px; top: 38px; }
  .card--front .tagline { left: 262px; top: 76px; }
  .person { position: absolute; left: 196px; top: 122px; }
  .person__name { font-size: 24px; color: var(--ink-navy); line-height: 1.1; }
  .person__role { font-size: 14px; color: var(--accent-blue); margin-top: 2px; }
  .divider {
    position: absolute; left: 338px; top: 122px;
    width: 1px; height: 66px; background: var(--rule-grey);
  }
  .contact {
    position: absolute; left: 352px; top: 136px;
    font-size: 13px; color: var(--accent-blue); line-height: 1.5;
  }
  .card--back .brand { left: 236px; top: 48px; }
  .card--back .tagline { left: 280px; top: 86px; }
  .card--back .website { left: 280px; top: 108px; }
</style>
</head>
<body>
<main class="canvas">

  <section class="card card--front" aria-label="Business card, front">
    <svg class="card__band" viewBox="0 0 520 300" aria-hidden="true">
      <path d="M0,0 L40,0 C90,150 260,250 520,270 L520,300 L0,300 Z" fill="var(--brand-blue)"/>
      <path d="M40,0 C90,150 260,250 520,270" fill="none" stroke="var(--band-grey)" stroke-width="7"/>
    </svg>
    <div class="brand">
      <span class="brand__dot"></span>
      <span class="brand__name">Kovenda Group</span>
    </div>
    <p class="tagline">Business Services</p>
    <div class="person">
      <p class="person__name">Your Name</p>
      <p class="person__role">Your Position</p>
    </div>
    <span class="divider"></span>
    <div class="contact">
      <p>Cellphone Number</p>
      <p>Personal e-mail</p>
    </div>
  </section>

  <section class="card card--back" aria-label="Business card, back">
    <svg class="card__band" viewBox="0 0 520 300" aria-hidden="true">
      <path d="M0,0 L40,0 C90,150 260,250 520,270 L520,300 L0,300 Z" fill="var(--brand-blue)"/>
      <path d="M40,0 C90,150 260,250 520,270" fill="none" stroke="var(--band-grey)" stroke-width="7"/>
    </svg>
    <div class="brand">
      <span class="brand__dot"></span>
      <span class="brand__name">Kovenda Group</span>
    </div>
    <p class="tagline">Business Services</p>
    <p class="website">www.kovendagroup.com</p>
  </section>

</main>
</body>
</html>
```